Verlane Area Planning Council Business Cards

We're looking for a business card design, simple as that. We're a local government agency that mainly performs building code enforcement, transportation planning, floodplain management, and GIS for Tobinet Parish in Louisiana, and other surround parishes. So you're not having to Google anything, GIS is, at it's core, mapping. Building Code Enforcement is just that, nothing more. Floodplain Management is to make sure the public is within what the government

Contact Information for Business Card

Our Address is

417 Merriwell Avenue
Corvel City, ST 70000

Our phone is 5550192734
Our fax is 5550192739
Our website is www.vlpk.example
My email is dana@vlpk.example

Font styles to use
Serif
Sans Serif

Colors

Designer to choose colors to be used in the design.

Requirements
Must have
• I'm attaching our logo(several versions) that must be incorporated. The design should fit well with our existing logo. I can send photoshop files for our logo if needed. If possible, I'd like to be able to add names/info to each card for all of our employees once this is done.
Nice to have
• The Regional emblem is a bonus, and isn't specifically required.

```html
<!DOCTYPE html>
<html lang="en">
<head>
<meta charset="utf-8">
<title>Verlane Area Planning Council – Business Cards</title>
<link rel="stylesheet" href="https://fonts.googleapis.com/css2?family=Bebas+Neue&family=Montserrat:wght@400;500;700&display=swap">
<style>
  :root {
    --stage: #4a4a4a;
    --card: #2c2c2c;
    --accent: #d8f20e;
    --white: #ffffff;
    --muted: #cfcfcf;
    --blue: #1f5fe0;
    --green: #2fae3a;
    --orange: #f28c1a;
    --emblem: #1d3f86;
  }
  * { box-sizing: border-box; margin: 0; padding: 0; }
  html, body { width: 1200px; height: 901px; overflow: hidden; }
  body {
    background: var(--stage);
    font-family: "Montserrat", sans-serif;
    color: var(--white);
    display: flex;
    flex-direction: column;
    align-items: center;
    justify-content: center;
    gap: 40px;
  }
  .card {
    position: relative;
    width: 660px;
    height: 377px;
    background: var(--card);
    border-bottom: 9px solid var(--accent);
    box-shadow: 0 10px 24px rgba(0,0,0,.35);
  }
  .brand {
    position: absolute;
    left: 0; right: 0;
    display: flex;
    flex-direction: column;
    align-items: center;
  }
  .card--front .brand { top: 120px; }
  .card--back .brand { top: 34px; }
  .brand__mark {
    display: flex;
    align-items: center;
    gap: 16px;
  }
  .brand__square {
    width: 58px; height: 58px;
    background: var(--accent);
  }
  .brand__name {
    font-weight: 700;
    font-size: 78px;
    line-height: 1;
    letter-spacing: 2px;
    color: var(--white);
  }
  .brand__tagline {
    margin-top: 8px;
    font-size: 15px;
    font-weight: 400;
    letter-spacing: .5px;
    color: var(--muted);
  }
  .person {
    position: absolute;
    top: 192px;
    right: 352px;
    text-align: right;
  }
  .person__name {
    font-family: "Bebas Neue", sans-serif;
    font-size: 50px;
    line-height: 1;
    color: var(--accent);
  }
  .person__role {
    font-size: 18px;
    font-weight: 500;
  }
  .divider {
    position: absolute;
    top: 186px;
    left: 330px;
    width: 1.5px;
    height: 100px;
    background: var(--muted);
  }
  .contacts {
    position: absolute;
    top: 186px;
    left: 350px;
    list-style: none;
  }
  .contacts li {
    display: flex;
    align-items: center;
    gap: 10px;
    font-size: 18px;
    font-weight: 500;
    line-height: 25px;
  }
  .contacts svg { width: 18px; height: 18px; flex: none; }
  .address {
    position: absolute;
    left: 110px;
    bottom: 26px;
    font-size: 18px;
    font-weight: 500;
  }
  .emblem {
    position: absolute;
    right: 22px;
    bottom: 16px;
    width: 58px; height: 58px;
    border-radius: 50%;
    background: var(--emblem);
    border: 4px solid var(--white);
  }
</style>
</head>
<body>

  <section class="card card--front">
    <div class="brand">
      <div class="brand__mark">
        <span class="brand__square"></span>
        <span class="brand__name">VLPK</span>
      </div>
      <p class="brand__tagline">Verlane Area Planning Council</p>
    </div>
  </section>

  <section class="card card--back">
    <div class="brand">
      <div class="brand__mark">
        <span class="brand__square"></span>
        <span class="brand__name">VLPK</span>
      </div>
      <p class="brand__tagline">Verlane Area Planning Council</p>
    </div>

    <div class="person">
      <p class="person__name">Casey Reed</p>
      <p class="person__role">Manager</p>
    </div>

    <span class="divider"></span>

    <ul class="contacts">
      <li>
        <svg viewBox="0 0 24 24" aria-hidden="true"><path fill="var(--blue)" d="M6.6 10.8a15 15 0 0 0 6.6 6.6l2.2-2.2a1 1 0 0 1 1-.25 11.4 11.4 0 0 0 3.6.57 1 1 0 0 1 1 1V20a1 1 0 0 1-1 1A17 17 0 0 1 3 4a1 1 0 0 1 1-1h3.5a1 1 0 0 1 1 1c0 1.25.2 2.45.57 3.570a1 1 0 0 1-.25 1z"/></svg>
        5550192734
      </li>
      <li>
        <svg viewBox="0 0 24 24" aria-hidden="true"><g fill="var(--green)"><rect x="6" y="2" width="12" height="6"/><rect x="2" y="9" width="20" height="9" rx="2"/><rect x="6" y="15" width="12" height="7" fill="var(--card)" stroke="var(--green)" stroke-width="2"/></g></svg>
        5550192739
      </li>
      <li>
        <svg viewBox="0 0 24 24" aria-hidden="true"><rect x="2" y="5" width="20" height="14" fill="var(--orange)"/><path d="M2 5l10 8 10-8" fill="none" stroke="var(--card)" stroke-width="1.6"/></svg>
        dana@vlpk.example
      </li>
      <li>
        <svg viewBox="0 0 24 24" aria-hidden="true"><g fill="none" stroke="var(--accent)" stroke-width="2"><circle cx="12" cy="12" r="9"/><path d="M3 12h18M12 3c3 3 3 15 0 18M12 3c-3 3-3 15 0 18"/></g></svg>
        www.vlpk.example
      </li>
    </ul>

    <p class="address">417 Merriwell Avenue, Corvel City, ST 70000</p>

    <span class="emblem" role="img" aria-label="Regional emblem"></span>
  </section>

</body>
</html>
```